Company letter head and business card for new Indian Pharmaceutical Export company.

We need a letterhead and business card design for an Indian Pharmaceutical Export company.

The letter head needs to contain the following information.
Vorin Healthline Pvt. Ltd.
Office No 4827 Plot No 19, Larkspire, KT Lane, 400153, Maharashtra, India.
Email: info@vorin-healthline.com
Phone: +91-8342196507
CIN: U71853MH2025PTC902617
GSTIN: (This number is still pending, we will add later)

The business card needs to contain:
Address:
Vorin Healthline Pvt. Ltd.
Office No 4827 Plot No19, Larkspire, KT Lane, 400153, MH, India.
Email: torvald@vorin-healthline.com
Phone: +49-17634902851
Name on card: Torvald Ramming
Position: Director

The design for the letter head and business card should be simple but trustworthy.
Please use only Green and blue, same as in the attached logo.

```html
<!DOCTYPE html>
<html lang="en">
<head>
<meta charset="utf-8">
<title>Vorin Healthline – Business Card</title>
<link href="https://fonts.googleapis.com/css2?family=Arimo:wght@400;700&family=Montserrat:wght@700&display=swap" rel="stylesheet">
<style>
  :root {
    --brand-blue: #0b5fa5;
    --brand-green: #8dc63f;
    --text-grey: #555555;
    --divider-grey: #8a8a8a;
    --card-white: #ffffff;
    --page-bg: #e9e9e9;
  }
  * { margin: 0; padding: 0; box-sizing: border-box; }
  html, body {
    width: 1125px; height: 1200px; overflow: hidden;
    background: var(--page-bg);
  }
  .canvas { position: relative; width: 1125px; height: 1200px; }

  .card {
    position: absolute; left: 150px; width: 825px; height: 472px;
    border-radius: 26px; overflow: hidden;
  }
  .card-front { top: 98px; background: var(--card-white); }
  .card-back  { top: 631px; background: var(--brand-blue); }

  .front-waves { position: absolute; left: 0; top: 0; width: 825px; height: 472px; }

  .brand-block {
    position: absolute; left: 77px; top: 115px; width: 280px;
    display: flex; flex-direction: column; align-items: center;
  }
  .brand-dot {
    width: 150px; height: 150px; border-radius: 50%;
    background: var(--brand-blue);
  }
  .brand-name {
    margin-top: 22px;
    font-family: 'Montserrat', sans-serif; font-weight: 700;
    font-size: 23px; color: var(--brand-blue); white-space: nowrap;
  }

  .divider {
    position: absolute; left: 412px; top: 117px; width: 2px; height: 236px;
    background: var(--divider-grey);
  }

  .contact-block {
    position: absolute; left: 435px; top: 112px;
    font-family: 'Arimo', sans-serif; color: var(--text-grey);
  }
  .person-name { font-size: 26px; font-weight: 700; color: var(--brand-blue); line-height: 30px; letter-spacing: 0.2px; }
  .person-title { font-size: 23px; color: var(--brand-green); line-height: 30px; }
  .address { margin-top: 16px; font-size: 23px; line-height: 29.5px; }
  .contact-list { margin-top: 14px; list-style: none; font-size: 23px; line-height: 30px; }
  .contact-list li { display: flex; align-items: center; gap: 8px; }
  .contact-icon { width: 20px; height: 20px; flex: none; }

  .back-name {
    position: absolute; left: 0; right: 0; top: 198px; text-align: center;
    font-family: 'Montserrat', sans-serif; font-weight: 700;
    font-size: 57px; color: var(--card-white); line-height: 80px;
  }
</style>
</head>
<body>
<div class="canvas">

  <section class="card card-front" aria-label="Business card front">
    <svg class="front-waves" viewBox="0 0 825 472" aria-hidden="true">
      <path fill="var(--brand-green)" d="M0 398 C 110 385, 200 395, 280 420 C 190 408, 90 405, 0 418 Z"/>
      <path fill="var(--brand-green)" d="M550 448 C 660 444, 760 430, 825 412 L825 430 C 760 448, 660 455, 550 448 Z"/>
      <path fill="var(--brand-blue)" d="M0 428 C 90 408, 200 412, 330 428 C 470 444, 580 458, 690 457 C 760 456, 800 446, 825 438 L825 472 L0 472 Z"/>
    </svg>

    <div class="brand-block">
      <div class="brand-dot"></div>
      <div class="brand-name">Vorin Healthline</div>
    </div>

    <div class="divider"></div>

    <div class="contact-block">
      <div class="person-name">TORVALD RAMMING</div>
      <div class="person-title">Director</div>
      <address class="address" style="font-style:normal">
        Office No 4827 Plot No19<br>
        Larkspire, KT Lane<br>
        400153, MH, India
      </address>
      <ul class="contact-list">
        <li>
          <svg class="contact-icon" viewBox="0 0 20 20" aria-hidden="true">
            <path fill="var(--brand-green)" d="M2 7 C2 3, 18 3, 18 7 L15 8 L14 6 C12 5.3, 8 5.3, 6 6 L5 8 Z"/>
            <path fill="var(--brand-green)" d="M6 9 L14 9 L17 16 L3 16 Z"/>
            <circle cx="10" cy="12.5" r="2" fill="#fff"/>
          </svg>
          +49-17634902851
        </li>
        <li>
          <svg class="contact-icon" viewBox="0 0 20 20" aria-hidden="true">
            <path fill="var(--brand-green)" d="M2 8 L10 2 L18 8 L18 18 L2 18 Z"/>
            <path fill="none" stroke="#fff" stroke-width="1.4" d="M2 8 L10 13 L18 8 M2 18 L8 12 M18 18 L12 12"/>
          </svg>
          torvald@vorin-healthline.com
        </li>
      </ul>
    </div>
  </section>

  <section class="card card-back" aria-label="Business card back">
    <div class="back-name">Vorin Healthline</div>
  </section>

</div>
</body>
</html>
```